Personal Business Card Design Project

I am looking for a business card to be able to hand to both Chinese and Australian businessman.
I am a self employed consultant and just need my name, phone number and email address on the card. No Business Name and No Website.
I want it to look like an exclusive prestigious card.
I would like the background to be be a glossy red and the writing to be gold. (This applies to both sides of the card).
It must have English on one side and Chinese (Mandarin) on the reverse.
Details you will require
Name : Wade Emmerson
Phone : + 61 493 207 158
Email : wadeyemmerson@brightpost.example
Thank you everybody for your designs.
Industry/Entity Type
Business

```html
<!DOCTYPE html>
<html lang="en">
<head>
<meta charset="utf-8">
<title>Wade Emmerson – Business Cards</title>
<link rel="stylesheet" href="https://fonts.googleapis.com/css2?family=Noto+Sans+SC:wght@200&family=Noto+Serif:ital,wght@0,400;0,700;1,400&display=swap">
<style>
  :root {
    --page: #ffffff;
    --gold: #ffd400;
    --red: #e00000;
    --red-shade: rgba(150, 40, 50, 0.28);
    --shadow: rgba(0, 0, 0, 0.4);
  }
  * { margin: 0; padding: 0; box-sizing: border-box; }
  html, body {
    width: 963px;
    height: 1200px;
    overflow: hidden;
    background: var(--page);
  }
  .canvas {
    position: relative;
    width: 963px;
    height: 1200px;
  }
  .card {
    position: absolute;
    background: var(--gold);
    box-shadow: 7px 7px 7px var(--shadow);
  }
  .card--chinese { left: 116px; top: 136px; width: 681px; height: 417px; }
  .card--english { left: 109px; top: 583px; width: 690px; height: 422px; }
  .card__face {
    position: absolute;
    inset: 21px;
    background: var(--red);
    overflow: hidden;
  }
  .card__texture {
    position: absolute;
  }
  .card--chinese .card__texture {
    left: 0; top: 0; width: 360px; height: 100%;
    background: radial-gradient(ellipse at 30% 40%, var(--red-shade), transparent 70%);
  }
  .card--english .card__texture {
    right: 0; top: 0; width: 380px; height: 100%;
    background: radial-gradient(ellipse at 60% 50%, var(--red-shade), transparent 70%);
  }
  .details {
    position: absolute;
    display: flex;
    flex-direction: column;
    color: var(--gold);
    font-family: "Noto Serif", Georgia, serif;
  }
  .card--chinese .details { right: 43px; top: 170px; align-items: flex-end; text-align: right; }
  .card--english .details { left: 73px; top: 198px; align-items: flex-start; }
  .details__title-zh {
    font-family: "Noto Sans SC", sans-serif;
    font-weight: 200;
    font-size: 60px;
    line-height: 1;
  }
  .details__title-en {
    font-size: 27px;
    line-height: 1.1;
  }
  .details__rule {
    width: 36px;
    height: 3px;
    background: var(--gold);
    margin: 9px 0 5px;
  }
  .details__rule--end { margin: 16px 0 0; }
  .details__name {
    font-weight: 700;
    font-size: 29px;
    line-height: 1.1;
  }
  .details__phone {
    font-size: 19px;
    line-height: 1.05;
  }
  .details__email {
    font-style: italic;
    font-size: 19px;
    line-height: 1.15;
  }
</style>
</head>
<body>
<main class="canvas">
  <section class="card card--chinese" lang="zh">
    <div class="card__face">
      <div class="card__texture" role="img" aria-label="Faint scattered star pattern in deep red"></div>
      <div class="details">
        <p class="details__title-zh">顾问</p>
        <span class="details__rule"></span>
        <p class="details__name">Wade Emmerson</p>
        <p class="details__phone">+ 61 493 207 158</p>
        <p class="details__email">wadeyemmerson@brightpost.example</p>
        <span class="details__rule details__rule--end"></span>
      </div>
    </div>
  </section>

  <section class="card card--english" lang="en">
    <div class="card__face">
      <div class="card__texture" role="img" aria-label="Faint scattered star pattern in deep red"></div>
      <div class="details">
        <p class="details__title-en">Business Consultant</p>
        <span class="details__rule"></span>
        <p class="details__name">Wade Emmerson</p>
        <p class="details__phone">+ 61 493 207 158</p>
        <p class="details__email">wadeyemmerson@brightpost.example</p>
        <span class="details__rule details__rule--end"></span>
      </div>
    </div>
  </section>
</main>
</body>
</html>
```